Veltrano - Mechanic/Collision Center Business Card

We're looking for a business card design for our mechanic/ collision repair shop.

Can be with colours or monochromatic.

See the attached files.

Many thanks

```html
<!DOCTYPE html>
<html lang="en">
<head>
<meta charset="UTF-8">
<title>Veltrano Business Card</title>
<link href="https://fonts.googleapis.com/css2?family=Lato:wght@400;700;900&display=swap" rel="stylesheet">
<style>
  :root {
    --backdrop: #2b2c2e;
    --card-dark: #1e1f21;
    --card-light: #ffffff;
    --brand-blue: #2a9ad9;
    --ink: #1f2023;
    --ink-soft: #3a3b3e;
  }
  * { margin: 0; padding: 0; box-sizing: border-box; }
  html, body {
    width: 1200px; height: 900px; overflow: hidden;
    background: var(--backdrop);
    font-family: "Lato", sans-serif;
  }
  .canvas {
    position: relative; width: 1200px; height: 900px;
  }
  .card {
    position: absolute; left: 250px; width: 700px; height: 400px;
    overflow: hidden;
    box-shadow: 0 10px 30px rgba(0,0,0,0.45);
  }
  /* Back side */
  .card-back { top: 40px; background: var(--card-dark); }
  .card-back .wordmark {
    position: absolute; left: 0; right: 0; top: 140px;
    display: flex; justify-content: center; align-items: center; gap: 18px;
  }
  .wordmark-dot {
    width: 26px; height: 26px; border-radius: 50%; background: var(--brand-blue);
  }
  .wordmark-name {
    font-weight: 900; font-size: 64px; letter-spacing: 2px; text-transform: uppercase;
  }
  .card-back .wordmark-name { color: #ffffff; }
  .card-back .website {
    position: absolute; left: 0; right: 0; top: 280px; text-align: center;
    color: #ffffff; font-size: 20px; letter-spacing: 1.5px;
  }
  /* Front side */
  .card-front { top: 470px; background: var(--card-light); }
  .card-front .swoosh { position: absolute; inset: 0; }
  .card-front .wordmark {
    position: absolute; left: 40px; top: 110px; width: 330px;
    display: flex; justify-content: center; align-items: center; gap: 12px;
  }
  .card-front .wordmark-name { color: var(--ink); font-size: 44px; }
  .card-front .wordmark-dot { width: 18px; height: 18px; }
  .divider {
    position: absolute; left: 400px; top: 60px; width: 2px; height: 175px;
    background: var(--brand-blue);
  }
  .contact {
    position: absolute; left: 440px; top: 62px; color: var(--ink);
  }
  .contact-name { color: var(--brand-blue); font-weight: 700; font-size: 30px; line-height: 1.1; }
  .contact-role { font-size: 18px; color: var(--ink-soft); margin-bottom: 12px; }
  .contact-address { font-size: 19px; line-height: 1.3; margin-bottom: 8px; }
  .contact-line { display: flex; align-items: center; gap: 10px; font-size: 19px; line-height: 1.45; }
  .contact-line svg { width: 16px; height: 16px; fill: var(--brand-blue); flex: none; }
  .card-front .website {
    position: absolute; left: 80px; top: 330px; color: #ffffff; font-size: 20px; letter-spacing: 1.5px;
  }
</style>
</head>
<body>
<div class="canvas">
  <section class="card card-back">
    <div class="wordmark">
      <span class="wordmark-dot"></span>
      <span class="wordmark-name">Veltrano</span>
    </div>
    <p class="website">www.veltrano.com</p>
  </section>

  <section class="card card-front">
    <svg class="swoosh" viewBox="0 0 700 400" width="700" height="400" aria-hidden="true">
      <path d="M0,232 Q360,282 700,380 L700,400 L655,400 Q350,292 0,246 Z" fill="var(--brand-blue)"/>
      <path d="M0,252 Q340,296 630,400 L0,400 Z" fill="var(--card-dark)"/>
    </svg>
    <div class="wordmark">
      <span class="wordmark-dot"></span>
      <span class="wordmark-name">Veltrano</span>
    </div>
    <div class="divider"></div>
    <div class="contact">
      <p class="contact-name">Daniel Hartwell</p>
      <p class="contact-role">Manager</p>
      <p class="contact-address">418 Cedar Mill Road<br>Houston, TX 77041</p>
      <p class="contact-line">
        <svg viewBox="0 0 16 16"><path d="M3.5 1 L6 1 L7 5 L5.3 6.3 Q6.6 9.4 9.7 10.7 L11 9 L15 10 L15 12.5 Q15 15 12.5 15 Q1 14 1 3.5 Q1 1 3.5 1 Z"/></svg>
        555 014 2290
      </p>
      <p class="contact-line">
        <svg viewBox="0 0 16 16"><rect x="4" y="1" width="8" height="4"/><rect x="1" y="6" width="14" height="6" rx="1"/><rect x="4" y="10" width="8" height="5" fill="#fff" stroke="var(--brand-blue)" stroke-width="1.5"/></svg>
        555 014 2291
      </p>
      <p class="contact-line">
        <svg viewBox="0 0 16 16"><rect x="1" y="3" width="14" height="10"/><path d="M1 3 L8 9 L15 3" fill="none" stroke="#fff" stroke-width="1.4"/></svg>
        info@veltrano.com
      </p>
    </div>
    <p class="website">www.veltrano.com</p>
  </section>
</div>
</body>
</html>
```